Photographer website

This website will contain information to sell the services of marvello tebani an up and coming photographer based in london

Target Market(s)

SME's for corporate head shots
mums for kids parties
actors - for headshots
up and coming models

Industry/Entity Type

Photographer

Number of Pages Required

3 page

Requirements
Must have
• Home
• About me
• Contact me
• Portfolio or gallery

```html
<!DOCTYPE html>
<html lang="en">
<head>
<meta charset="utf-8">
<title>Marvello Tebani — Photographer</title>
<link rel="stylesheet" href="https://fonts.googleapis.com/css2?family=Open+Sans:wght@300&family=Raleway:wght@400;500&family=Lora:ital@1&display=swap">
<style>
  :root {
    --page-black: #000000;
    --sidebar: #111111;
    --panel: #ffffff;
    --nav-text: #d9d9d9;
    --caret: #8a8a8a;
    --muted: #6f6f6f;
    --heading: #2b2b2b;
    --body-text: #6a6a6a;
    --accent: #f3e36f;
    --icon: #444444;
    --side-icon: #6a6a6a;
    --copyright: #3a3a3a;
  }
  * { box-sizing: border-box; margin: 0; padding: 0; }
  html, body { width: 1200px; height: 589px; overflow: hidden; background: var(--page-black); }
  .site { position: relative; width: 1200px; height: 589px; background: var(--page-black); font-family: "Raleway", sans-serif; }

  .sidebar { position: absolute; left: 21px; top: 21px; width: 159px; height: 546px; background: var(--sidebar); text-align: center; }
  .brand { position: absolute; left: 0; right: 0; top: 90px; color: #ffffff; font-weight: 400; font-size: 20px; letter-spacing: 1px; line-height: 24px; }
  .main-nav { position: absolute; left: 0; right: 0; top: 188px; list-style: none; }
  .main-nav li { color: var(--nav-text); font-size: 11px; font-weight: 500; letter-spacing: 0.8px; line-height: 23.2px; text-transform: uppercase; }
  .main-nav .caret { width: 6px; height: 4px; margin-left: 3px; vertical-align: 2px; }
  .side-social { position: absolute; left: 0; right: 0; top: 352px; display: flex; justify-content: center; gap: 12px; }
  .social-dot { width: 10px; height: 10px; border-radius: 50%; background: var(--side-icon); }
  .copyright { position: absolute; left: 0; right: 0; top: 372px; color: var(--copyright); font-size: 9.5px; letter-spacing: 0.5px; }

  .portrait { position: absolute; left: 180px; top: 21px; width: 500px; height: 546px;
    background: radial-gradient(ellipse at 55% 30%, #9a9a9a 0%, #5c5c5c 45%, #2a2a2a 100%); }

  .about { position: absolute; left: 680px; top: 21px; width: 499px; height: 546px; background: var(--panel); }
  .about-title { position: absolute; left: 35px; top: 38px; font-family: "Open Sans", sans-serif; font-weight: 300; font-size: 23px; letter-spacing: 2px; color: var(--heading); text-transform: uppercase; }
  .about-text { position: absolute; left: 35px; top: 99px; width: 422px; font-size: 11.6px; line-height: 21.3px; color: var(--body-text); }
  .contact-block { position: absolute; left: 35px; top: 305px; width: 300px; height: 110px; border-left: 4px solid var(--accent); padding: 17px 0 0 28px; }
  .contact-label { font-family: "Lora", serif; font-style: italic; font-size: 11.5px; color: var(--muted); }
  .contact-social { display: flex; gap: 13px; margin-top: 19px; margin-left: -4px; }
  .contact-social .social-dot { background: var(--icon); width: 11px; height: 11px; }
</style>
</head>
<body>
<div class="site">
  <aside class="sidebar">
    <div class="brand">Tebani</div>
    <ul class="main-nav">
      <li>Home <svg class="caret" viewBox="0 0 6 4"><path d="M0.5 0.5 L3 3 L5.5 0.5" fill="none" stroke="var(--caret)" stroke-width="1"/></svg></li>
      <li>Portfolio <svg class="caret" viewBox="0 0 6 4"><path d="M0.5 0.5 L3 3 L5.5 0.5" fill="none" stroke="var(--caret)" stroke-width="1"/></svg></li>
      <li>About <svg class="caret" viewBox="0 0 6 4"><path d="M0.5 0.5 L3 3 L5.5 0.5" fill="none" stroke="var(--caret)" stroke-width="1"/></svg></li>
      <li>Contact</li>
    </ul>
    <div class="side-social">
      <span class="social-dot"></span><span class="social-dot"></span><span class="social-dot"></span><span class="social-dot"></span>
    </div>
    <p class="copyright">© Tebani | 2016</p>
  </aside>

  <div class="portrait" role="img" aria-label="Black and white portrait photograph of a long-haired model in a patterned top, hand raised to her head"></div>

  <section class="about">
    <h1 class="about-title">Marvello Tebani</h1>
    <p class="about-text">Lorem ipsum dolor sit amet, consectetuer adipiscing elit. Morbi gravida libero nec velit. Morbi scelerisque luctus velit. Etiam dui sem, fermentum vitae, sagittis id, malesuada in, quam. Proin mattis lacinia justo. Vestibulum facilisis auctor urna. Aliquam in lorem sit amet leo accumsan lacinia. Integer rutrum, orci vestibulum ullamcorper ultricies, lacus quam ultricies odio, vitae placerat pede sem sit amet enim. Phasellus et lorem id felis nonummy placerat. Fusce dui leo, imperdiet in, aliquam sit amet, feugiat eu, orci. Aenean vel massa quis mauris vehicula lacinia. Quisque tincidunt scelerisque libero.</p>
    <div class="contact-block">
      <p class="contact-label">Contact me at:</p>
      <div class="contact-social">
        <span class="social-dot"></span><span class="social-dot"></span><span class="social-dot"></span><span class="social-dot"></span>
      </div>
    </div>
  </section>
</div>
</body>
</html>
```